Business Card for Flight Instructor/Commercial Pilot

I need a business card for myself as a Flight Instructor. I'm a certificated flight instructor at a local flight school in St Paul, MN and want to have a business card that I can give out both to prospective students and also to prospective employers in commercial/business aviation. The business card should have a few elements to it (my name, my position, and my ZRT certifications:
Dorian Welkes, MBA
Flight Instructor
CFI, CFII, AGI, IGI
Then lastly, I'd like it to include my phone number for calls or texts, my email address, and my Corvanet url. I'll provide all of these at a later point.

If we can include some kind of aviation graphic, that's great, but I don't currently have a logo and I don't necessarily need one, so don't feel like a logo is required here, it's not. I'm but I'm open to whatever you might put together. But I honestly don't need a logo, just good design with a simple graphic element to draw a little interest.
I'd also like to add a short tag line. A few ideas I have are:
- Fly Smart. Stay Humble. Never Stop Learning.
- Train smart. Fly safe. Have fun.
- Master the craft. Enjoy the flight.

For the back side, I'm open to ideas on what to put there. maybe the tagline could go there, or a QR code for my Corvanet page, or maybe something else.

Target audience is both prospective students who are interested in learning to fly (or adding more ratings) and commercial aviation companies that could be potential employer for me in commercial aviation. Trying to portray a sense of professionalism, trust, and high level of competency.

The business card doesn’t have to be standard (rectangular with square corners) and I’m open to suggestions for based on the design.
Lastly, I just don't want the design created by AI.
Let me know if you need any further info. Thanks!

```html
<!DOCTYPE html>
<html lang="en">
<head>
<meta charset="utf-8">
<title>Dorian Welkes, MBA — Business Card</title>
<link href="https://fonts.googleapis.com/css2?family=Arimo:ital,wght@0,700;1,700&family=Outfit:wght@400;500;700&display=swap" rel="stylesheet">
<style>
  :root {
    --board: #b5c6bd;
    --label: #3f5444;
    --card: #ffffff;
    --charcoal: #3c3d3c;
    --slate: #646c67;
    --sage: #c5ccb2;
    --gold: #e3d497;
    --ink: #151515;
    --ink-soft: #2c3a33;
    --plane: #97a3a0;
  }
  * { margin: 0; padding: 0; box-sizing: border-box; }
  html, body { width: 1200px; height: 999px; overflow: hidden; }
  body { background: var(--board); position: relative; font-family: "Outfit", sans-serif; }

  .side-label {
    position: absolute;
    left: 301px;
    font-family: "Outfit", sans-serif;
    font-weight: 700;
    font-size: 41px;
    letter-spacing: 1px;
    color: var(--label);
    line-height: 1;
  }
  .side-label--front { top: 52px; }
  .side-label--back { top: 508px; }

  .card {
    position: absolute;
    left: 296px;
    width: 620px;
    height: 354px;
    border-radius: 8px;
    overflow: hidden;
    background: var(--card);
    box-shadow: 16px 14px 18px rgba(40, 50, 45, 0.45);
  }
  .card--front { top: 104px; }
  .card--back { top: 560px; }
  .card svg { display: block; width: 100%; height: 100%; }

  .name { font-family: "Arimo", sans-serif; font-weight: 700; font-size: 58px; letter-spacing: 1.5px; fill: var(--ink); }
  .title { font-family: "Outfit", sans-serif; font-weight: 400; font-size: 32px; letter-spacing: 0.6px; fill: var(--ink-soft); }
  .contact { font-family: "Outfit", sans-serif; font-weight: 400; font-size: 28px; letter-spacing: 0.6px; fill: var(--gold); }
  .icon { fill: var(--gold); }
  .tagline { font-family: "Arimo", sans-serif; font-weight: 700; font-style: italic; fill: var(--ink); }
  .tagline--top { font-size: 42px; letter-spacing: 1px; }
  .tagline--main { font-size: 57px; letter-spacing: 1px; }
  .web-back { font-family: "Outfit", sans-serif; font-size: 33px; letter-spacing: 0.8px; fill: var(--gold); }
</style>
</head>
<body>

<div class="side-label side-label--front">FRONT SIDE</div>
<section class="card card--front" aria-label="Business card front">
  <svg viewBox="0 0 1084 620" xmlns="http://www.w3.org/2000/svg">
    <path fill="var(--sage)" d="M0,228 C300,215 600,300 935,620 L0,620 Z"/>
    <path fill="var(--slate)" d="M0,258 C300,245 600,330 920,620 L0,620 Z"/>
    <path fill="var(--charcoal)" d="M0,305 C320,280 620,360 905,620 L0,620 Z"/>
    <path fill="var(--charcoal)" d="M707,430 C780,455 850,455 900,450 C980,445 1040,415 1084,380 L1084,620 L958,620 C880,540 800,480 707,430 Z"/>

    <text class="name" x="550" y="125" text-anchor="middle">Dorian Welkes, MBA</text>
    <line x1="254" y1="138" x2="845" y2="138" stroke="var(--slate)" stroke-width="2"/>
    <text class="title" x="550" y="175" text-anchor="middle">Flight Instructor CFI, CFII, AGI, IGI</text>

    <path class="icon" d="M62,373 l8,-4 l8,13 l-6,4 c3,6 7,10 12,13 l5,-5 l12,9 l-4,8 c-16,2 -36,-20 -35,-38 Z"/>
    <text class="contact" x="104" y="398">+1651555014207</text>
    <rect class="icon" x="60" y="417" width="30" height="19" rx="1"/>
    <path d="M61,418 L75,429 L89,418" fill="none" stroke="var(--charcoal)" stroke-width="2"/>
    <text class="contact" x="104" y="435">dorian_welkes@welkesaviation.com</text>
    <g fill="none" stroke="var(--gold)" stroke-width="2">
      <circle cx="75" cy="466" r="13"/>
      <ellipse cx="75" cy="466" rx="6" ry="13"/>
      <line x1="62" y1="466" x2="88" y2="466"/>
      <line x1="64" y1="459" x2="86" y2="459"/>
      <line x1="64" y1="473" x2="86" y2="473"/>
    </g>
    <text class="contact" x="104" y="475">www.welkesaviation.com</text>
    <path class="icon" d="M76,495 c-8,0 -13,6 -13,13 c0,9 13,21 13,21 c0,0 13,-12 13,-21 c0,-7 -5,-13 -13,-13 Z"/>
    <circle cx="76" cy="507" r="4.5" fill="var(--charcoal)"/>
    <text class="contact" x="104" y="521">Northfield Air Services</text>
    <text class="contact" x="104" y="555">STP, 240 Harbor Ln, St Paul, MN 55107</text>
  </svg>
</section>

<div class="side-label side-label--back">BACK SIDE</div>
<section class="card card--back" aria-label="Business card back">
  <svg viewBox="0 0 1084 620" xmlns="http://www.w3.org/2000/svg">
    <path fill="var(--slate)" d="M0,260 C120,440 300,500 450,492 C560,485 650,460 723,428 C620,480 450,540 300,540 C170,540 70,500 0,475 Z"/>
    <path fill="var(--sage)" d="M0,475 C70,500 170,540 300,540 C450,540 620,480 723,428 C620,490 450,560 300,560 C170,560 70,520 0,505 Z"/>
    <path fill="var(--charcoal)" d="M0,525 C180,590 300,600 420,575 C600,540 800,410 950,365 C1000,355 1050,358 1084,358 L1084,620 L0,620 Z"/>

    <text class="tagline tagline--top" x="492" y="160" text-anchor="middle">Fly Smart · Stay Humble</text>
    <line x1="199" y1="185" x2="760" y2="185" stroke="var(--ink-soft)" stroke-width="2"/>
    <text class="tagline tagline--main" x="485" y="241" text-anchor="middle">Never Stop Learning</text>

    <path fill="var(--plane)" d="M766,164 L772,164 L780,173 L812,173 L800,148 L812,148 L842,173 L895,174 C905,175 905,188 895,189 L790,189 C782,189 776,184 772,178 L762,176 Z"/>

    <text class="web-back" x="1034" y="555" text-anchor="end">www.welkesaviation.com</text>
  </svg>
</section>

</body>
</html>
```